corvana ridge bathrooms

We are in the business of renovating peoples bathrooms and tiling service

we provide a total solution from design to reconstruction of your bathroom

we would like a 5 page website

please design the home page first so we choose design then complete the other 4 pages i have uploaded the logo

Industry/Entity Type

Business

```html
<!DOCTYPE html>
<html lang="en">
<head>
<meta charset="utf-8">
<title>Corvana Ridge Bathrooms</title>
<link href="https://fonts.googleapis.com/css2?family=Cinzel:wght@500;600;700&family=Open+Sans:ital,wght@0,400;0,600;0,700;1,400&display=swap" rel="stylesheet">
<style>
:root{
  --brown-top:#6a3727;
  --brown-bottom:#4c2619;
  --gold:#b08a22;
  --gold-light:#e4b44c;
  --gold-dark:#c08a20;
  --gold-text:#a8882a;
  --ink:#2a1a10;
  --nav-ink:#3a2410;
  --body-text:#3a3a3a;
  --cream:#f5eec0;
  --paper:#fbfaf6;
  --footer:#363636;
  --footer-line:#555;
  --footer-text:#bdbdbd;
  --base:#222;
}
*{margin:0;padding:0;box-sizing:border-box}
html,body{width:1092px;height:1200px;overflow:hidden}
body{position:relative;font-family:"Open Sans",Arial,sans-serif;background:linear-gradient(#f6efbf 120px,#f8f4d8 300px,#fbfaf4 560px,#fff 900px);color:var(--body-text)}
.abs{position:absolute}
.header{left:0;top:0;width:1092px;height:118px;background:linear-gradient(var(--brown-top),var(--brown-bottom));border-bottom:5px solid #e9ddb6}
.nav{left:152px;top:58px;width:790px;height:46px;border-radius:6px;background:linear-gradient(#efc25a,var(--gold-dark));box-shadow:0 2px 4px rgba(0,0,0,.35)}
.nav a{position:absolute;top:12px;font-family:"Cinzel",serif;font-weight:600;font-size:17px;color:var(--nav-ink);text-decoration:none;letter-spacing:.5px}
.nav .current{left:8px;top:8px;width:80px;height:30px;border-radius:5px;background:linear-gradient(#f1dfb6,#d7bd88);text-align:center;padding-top:4px;color:#5a3a20}
.brand{left:452px;top:15px;width:190px;height:125px;border-radius:95px 95px 0 0;background:#fff;box-shadow:0 0 6px rgba(0,0,0,.25);text-align:center}
.brand .mark{width:14px;height:14px;border-radius:50%;background:var(--gold);margin:44px auto 10px}
.brand .name{font-family:"Cinzel",serif;font-weight:700;font-size:13px;line-height:16px;color:var(--ink)}
.slider{left:150px;top:140px;width:793px;height:399px;background:#d9cdb6;box-shadow:0 1px 3px rgba(0,0,0,.3)}
.slide-photo{left:9px;top:8px;width:776px;height:382px;background:linear-gradient(100deg,#d8b07a 0%,#caa06a 35%,#9fb3b8 60%,#d6b68c 80%,#b59066 100%)}
.caption{left:159px;top:298px;width:259px;height:158px;background:rgba(182,144,32,.88)}
.caption::after{content:"";position:absolute;right:-10px;top:68px;border:10px solid transparent;border-left-color:rgba(182,144,32,.88);border-right:0}
.caption h1{position:absolute;left:20px;top:19px;font-weight:600;font-size:20px;color:#fff;letter-spacing:-.3px}
.caption p{position:absolute;left:22px;top:54px;width:220px;font-size:10.5px;line-height:15.5px;color:#fff}
.caption .btn{position:absolute;left:23px;top:115px;width:70px;height:20px;background:#fff;border-radius:3px;font-size:8.5px;font-weight:700;color:#333;text-align:center;line-height:20px}
.dots{left:875px;top:513px}
.dots span{display:inline-block;width:10px;height:10px;border-radius:50%;background:#333;margin-right:8px;box-shadow:inset 0 0 0 2px #666}
h2.col-title{position:absolute;top:583px;font-family:"Cinzel",serif;font-weight:600;font-size:22px;color:var(--ink)}
.framed{background:#fff;border:1px solid #ddd;padding:4px}
.framed div{width:100%;height:100%}
.text{font-size:10px;line-height:16.5px;color:var(--body-text);letter-spacing:.1px}
.more{font-size:9.5px;color:var(--gold-text)}
.more::after{content:"›";margin-left:10px;color:#333;font-size:12px}
.svc-title{font-size:9.5px;font-weight:700;color:var(--gold-text)}
.svc-text{font-size:9.5px;line-height:16.5px;color:var(--gold-text)}
.date{width:37px;height:40px;background:var(--gold);color:#fff;text-align:center;border-radius:2px}
.date b{display:block;font-size:17px;line-height:22px;padding-top:2px}
.date small{display:block;font-size:7.5px;font-weight:700}
.news-title{font-size:9.5px;font-weight:700;color:var(--gold-text)}
.comments{font-size:8.5px;color:#888}
.footer{left:0;top:937px;width:1092px;height:228px;background:var(--footer);border-top:2px solid #4a4a4a}
.footer h3{position:absolute;top:30px;font-size:12.5px;font-weight:400;color:#eee}
.testimonial{left:176px;top:73px;width:126px;font-size:9.5px;font-style:italic;line-height:15.2px;color:#eee;text-align:justify}
.tweets{left:370px;top:70px;width:150px;font-size:9.5px;line-height:18.5px;color:var(--footer-text)}
.tweets .ago{color:#8fb6c9}
.socials{left:571px;top:64px;width:135px;list-style:none;border-top:1px solid var(--footer-line)}
.socials li{height:27px;border-bottom:1px solid var(--footer-line);font-size:9.5px;color:var(--footer-text);padding:6px 0 0 8px}
.contact{left:787px;top:64px;width:135px;border-top:1px solid var(--footer-line);border-bottom:1px solid var(--footer-line);height:80px;padding:12px 0 0 8px;font-size:9.5px;line-height:18px;color:var(--footer-text)}
.contact b{color:#eee;font-weight:600}
.ask{left:791px;top:160px;font-size:15px;font-weight:600;color:#fff;letter-spacing:-.8px}
.ask span{display:block;font-size:12px;font-weight:400;letter-spacing:4.5px;color:#ccc;margin-top:-1px}
.base{left:0;top:1165px;width:1092px;height:35px;background:var(--base);color:#fff;font-size:9px;font-weight:700;text-align:center;line-height:38px}
</style>
</head>
<body>
<header class="abs header"></header>
<nav class="abs nav">
  <a class="current" href="#">HOME</a>
  <a href="#" style="left:117px">ABOUT</a>
  <a href="#" style="left:213px">PROJECTS</a>
  <a href="#" style="left:495px">CLIENTS</a>
  <a href="#" style="left:590px">SERVICES</a>
  <a href="#" style="left:688px">CONTACT</a>
</nav>
<div class="abs brand">
  <div class="mark"></div>
  <div class="name">CORVANA RIDGE<br>BATHROOMS</div>
</div>

<section class="abs slider">
  <div class="abs slide-photo" role="img" aria-label="Sunlit marble bathroom with glass shower and sea-view windows"></div>
</section>
<div class="abs caption">
  <h1>Imagine your bathroom</h1>
  <p>Lorem ipsum dolor sit amet, consec tetuer adipiscing elit. Praesent vestibu lum moles Lorem ipsum dolor sit amet</p>
  <div class="btn">READ MORE</div>
</div>
<div class="abs dots"><span></span><span></span><span></span></div>

<h2 class="col-title" style="left:158px">Who We Are</h2>
<h2 class="col-title" style="left:440px">Services</h2>
<h2 class="col-title" style="left:716px">What’s New?</h2>

<div class="abs framed" style="left:158px;top:626px;width:215px;height:121px"><div role="img" aria-label="Bathroom with vanity, toilet and glass shower" style="background:linear-gradient(90deg,#b59a7a,#e6ddd0 45%,#cbbda8)"></div></div>
<p class="abs text" style="left:159px;top:756px;width:218px">Lorem ipsum dolor sit amet, consec tetuer adipi scing elit. Praesent vestibu lum mo lestie lacus. Aenean nonummy hendrerit mauris. Phasellus porta. Fusce suscipit varius um sociis natoque penatibusorbi nunc odio, gravida at, cursus nec, luctus</p>
<a class="abs more" style="left:159px;top:870px">More About Us</a>

<div class="abs framed" style="left:440px;top:626px;width:67px;height:66px"><div role="img" aria-label="Blue tiled shower" style="background:linear-gradient(135deg,#5d8fa6,#b9d3de)"></div></div>
<div class="abs svc-title" style="left:519px;top:633px">Renovation</div>
<div class="abs svc-text" style="left:519px;top:649px;width:140px">Lorem ipsum dolor sit amet, consectetuer adipiscing</div>
<div class="abs framed" style="left:440px;top:706px;width:67px;height:66px"><div role="img" aria-label="Framed artwork on a warm wall" style="background:linear-gradient(135deg,#6a4a30,#c9a57c)"></div></div>
<div class="abs svc-title" style="left:519px;top:713px">Design</div>
<div class="abs svc-text" style="left:519px;top:728px;width:140px">Lorem ipsum dolor sit amet, consectetuer adipiscing</div>
<div class="abs framed" style="left:440px;top:786px;width:67px;height:66px"><div role="img" aria-label="White vanity with blue tiles" style="background:linear-gradient(135deg,#4f7da0,#e3e8ec)"></div></div>
<div class="abs svc-title" style="left:519px;top:794px">Construction</div>
<div class="abs svc-text" style="left:519px;top:809px;width:140px">Lorem ipsum dolor sit amet, consectetuer adipi</div>
<a class="abs more" style="left:441px;top:870px">More Services</a>

<div class="abs date" style="left:716px;top:631px"><b>04</b><small>OCT</small></div>
<div class="abs news-title" style="left:762px;top:636px">Turning All Clients Into Dream Clients</div>
<p class="abs text" style="left:716px;top:677px;width:220px;line-height:14.5px">Lorem ipsum dolor sit amet, consec tetuer adipi scing elit. Praesent vestibu lum moles tie lacus. Aenean nonummyorem</p>
<div class="abs comments" style="left:716px;top:729px">35 Comments</div>
<div class="abs date" style="left:716px;top:760px"><b>28</b><small>SEP</small></div>
<div class="abs news-title" style="left:762px;top:765px">Creating Exclusive Concepts</div>
<p class="abs text" style="left:716px;top:806px;width:220px;line-height:14.5px">Lorem ipsum dolor sit amet, consec tetuer adipi scing elit. Praesent vestibu lum moles tie lacus. Aenean nonummyorem</p>
<div class="abs comments" style="left:716px;top:858px">25 Comments</div>

<footer class="abs footer">
  <h3 style="left:176px">Testimonials</h3>
  <h3 style="left:371px">Tweets</h3>
  <h3 style="left:579px">Socials</h3>
  <h3 style="left:791px">Get in touch</h3>
  <p class="abs testimonial">Lorem ipsum dolor sit amet, consec tetuer adipi scing elit. Praesent vestibu lum mo lestie lacus. Aenean nonummy hendrerit mauris. Phasellus porta. Fusce suscipit varius um sociis natoque penatibusorbi nunc odio, gravida at, cursus nec, luctus.<br><span style="display:block;text-align:right;margin-top:3px">@Mara Lindqvist</span></p>
  <div class="abs tweets">Lorem ipsum dolor sit amet, consectetur adipiscing lorem ipsum dolor sit amet.<br><span class="ago">@ 2 minutes ago</span><br><br>Tessel Studio on sales!<br><span class="ago">@ 15 minutes ago</span></div>
  <ul class="abs socials">
    <li>Subscribe feed</li>
    <li>Our Pagebook page</li>
    <li>Follow us on Chirper</li>
    <li>Snapshare</li>
  </ul>
  <div class="abs contact">Tessel Studio,<br>48 Harrow Lane NY<br><b>Phone:</b> + 39 340 5512904</div>
  <div class="abs ask">HAVE A QUESTION?<span>CONTACT US</span></div>
</footer>
<div class="abs base">CORVANA RIDGE BATHROOMS © 2012 © All Rights Reserved</div>
</body>
</html>
```